Local Flower Farm Needs Business Card Design

I need business cards designed for a flower farm based in Eudora, Kansas.
Business Info:
We are a local cut flower farm located in Eudora, Kansas, founded by Darla Hoffstrom. What started as a passion for agriculture and search for more joy in daily life has blossomed into a small business dedicated to providing the community with beautiful, fresh, and sustainable flowers. We specialize in local, seasonal blooms, ensuring that every petal reflects the care and dedication we pour into our craft. Our mission is to deliver the highest quality flowers directly to our customers through local farmers markets and to florists who share our commitment to sustainability. Join us in celebrating the beauty of nature, one bloom at a time!
Contact Details:
Darla Hoffstrom
Owner
Phone 913-555-0147
Facebook: Lorabelle Quinn Blossoms
Instagram: @LorabelleQuinnBlossoms
Website: LorabelleQuinnBlossoms.example
Target Market(s)
Wholesale to Florists and Direct to Consumer via Farmers Market
Industry/Entity Type
Florist, Farm
Contact Information for Business Card
Name, Contact Info, Logo
Look and feel

```html
<!DOCTYPE html>
<html lang="en">
<head>
<meta charset="utf-8">
<title>Lorabelle Quinn Blossoms – Business Card</title>
<link href="https://fonts.googleapis.com/css2?family=Arimo:wght@400;700&display=swap" rel="stylesheet">
<style>
  :root {
    --backdrop: #d9dbdc;
    --card: #f7f7f6;
    --ink: #17221f;
    --muted: #6c7170;
    --body: #3b403f;
    --faint: #ecedec;
    --shadow: rgba(0, 0, 0, 0.14);
  }
  * { box-sizing: border-box; margin: 0; padding: 0; }
  html, body {
    width: 1200px; height: 829px; overflow: hidden;
    background: var(--backdrop);
    font-family: "Arimo", Arial, sans-serif;
    color: var(--ink);
  }
  .stage {
    width: 1200px; height: 829px;
    display: flex; align-items: center; justify-content: center; gap: 60px;
  }
  .card {
    position: relative;
    width: 520px; height: 297px;
    background: var(--card);
    box-shadow: 0 10px 28px var(--shadow);
    overflow: hidden;
  }

  /* Front: contact column */
  .contact {
    position: absolute; left: 32px; top: 66px; width: 240px;
  }
  .contact__name {
    font-weight: 700; font-size: 20px; letter-spacing: 0.02em;
    text-transform: uppercase; line-height: 1.1;
  }
  .contact__role {
    font-size: 12.5px; color: var(--muted); margin-top: 3px;
  }
  .contact__rule {
    width: 10px; height: 1px; background: var(--muted); margin: 8px 0 10px;
  }
  .contact__list { list-style: none; }
  .contact__item {
    display: flex; align-items: center; gap: 7px;
    font-size: 13px; color: var(--body); line-height: 1.6;
    white-space: nowrap;
  }
  .contact__icon { width: 10px; height: 10px; flex: none; }

  /* Brand name block */
  .brand-area {
    position: absolute; top: 0; bottom: 0;
    display: flex; align-items: center; justify-content: center;
  }
  .card--front .brand-area { left: 290px; right: 24px; }
  .card--back .brand-area { left: 0; right: 0; }
  .brand {
    display: flex; align-items: center; gap: 10px;
  }
  .brand__dot {
    width: 16px; height: 16px; border-radius: 50%; background: var(--ink); flex: none;
  }
  .brand__name {
    font-size: 15px; font-weight: 400; letter-spacing: 0.1em;
    text-transform: uppercase; line-height: 1.4; color: var(--ink);
  }

  /* Back */
  .botanical-art {
    position: absolute; left: 30px; top: 0; width: 170px; height: 297px;
    background: linear-gradient(160deg, var(--faint), rgba(236, 237, 236, 0));
  }
</style>
</head>
<body>
<main class="stage">
  <section class="card card--front">
    <div class="contact">
      <h1 class="contact__name">Darla Hoffstrom</h1>
      <p class="contact__role">Owner</p>
      <div class="contact__rule"></div>
      <ul class="contact__list">
        <li class="contact__item">
          <svg class="contact__icon" viewBox="0 0 10 10" aria-hidden="true"><path d="M2 0.8 L3.6 0.8 L4.2 3 L3 3.8 Q4 6 6.2 7 L7 5.8 L9.2 6.4 L9.2 8 Q9.2 9.2 8 9.2 Q1 8.6 0.8 2 Q0.8 0.8 2 0.8Z" fill="#17221f"/></svg>
          913-555-0147
        </li>
        <li class="contact__item">
          <svg class="contact__icon" viewBox="0 0 10 10" aria-hidden="true"><circle cx="5" cy="5" r="4.5" fill="#17221f"/></svg>
          Lorabelle Quinn Blossoms
        </li>
        <li class="contact__item">
          <svg class="contact__icon" viewBox="0 0 10 10" aria-hidden="true"><rect x="1" y="1" width="8" height="8" rx="2" fill="none" stroke="#17221f" stroke-width="1.2"/></svg>
          @LorabelleQuinnBlossoms
        </li>
        <li class="contact__item">
          <svg class="contact__icon" viewBox="0 0 10 10" aria-hidden="true"><circle cx="5" cy="5" r="4.5" fill="#17221f"/></svg>
          LorabelleQuinnBlossoms.example
        </li>
      </ul>
    </div>
    <div class="brand-area">
      <div class="brand">
        <span class="brand__dot"></span>
        <span class="brand__name">Lorabelle Quinn<br>Blossoms</span>
      </div>
    </div>
  </section>

  <section class="card card--back">
    <div class="botanical-art" role="img" aria-label="Faint botanical line drawing of stems, leaves and blooms"></div>
    <div class="brand-area">
      <div class="brand">
        <span class="brand__dot"></span>
        <span class="brand__name">Lorabelle Quinn<br>Blossoms</span>
      </div>
    </div>
  </section>
</main>
</body>
</html>
```